Supplment jar label design (full label)

Hydration (blue) 300g –700ml jar, label size: 10 cm x 27 cm
make label for Kora Vital supps
needs to be full blown label that fits size I noted above
with all claims in attached doc
see attached product info and claims
see QDL & Ember attached as example of similar to what I want
carbon fibre background on label
I have also attached label example this is how i expect to receive designs
where is states SKU on label needs to be in colour above
needs files to able to customise with other SKUs in future
please message me if you have questions
Hydration

```html
<!DOCTYPE html>
<html lang="en">
<head>
<meta charset="utf-8">
<title>Kora Vital Hydration – Lemon Label</title>
<link rel="stylesheet" href="https://fonts.googleapis.com/css2?family=Archivo:wdth,wght@62..125,100..900&display=swap">
<style>
  :root {
    --page: #ffffff;
    --carbon-dark: #1f1f1f;
    --carbon-mid: #2e2e2e;
    --panel-grey: #e1e0dc;
    --band-grey: #dcdbd6;
    --lemon: #e9cd48;
    --ink: #111111;
    --white: #ffffff;
    --soft-white: #e8e8e8;
  }
  * { box-sizing: border-box; margin: 0; padding: 0; }
  html, body {
    width: 1199px; height: 1200px; overflow: hidden;
    background: var(--page);
    font-family: "Archivo", Arial, sans-serif;
  }
  .label {
    position: absolute; left: 54px; top: 398px;
    width: 1091px; height: 403px;
    overflow: hidden;
  }
  .carbon-fibre {
    position: absolute; inset: 0;
    background: linear-gradient(135deg, var(--carbon-mid), var(--carbon-dark) 55%, var(--carbon-mid));
  }
  .info-panel {
    position: absolute; left: 0; top: 0; width: 218px; height: 100%;
    background: var(--panel-grey);
    color: var(--ink);
    padding: 20px 14px;
    font-size: 10.5px; line-height: 1.3; text-align: center;
  }
  .info-panel p { margin-bottom: 11px; }
  .info-panel p.tight { margin-bottom: 0; }
  .brand-name {
    position: absolute; left: 296px; top: 26px;
    color: var(--white);
    font-weight: 800; font-stretch: 70%;
    font-size: 33px; line-height: 0.86; letter-spacing: -0.5px;
  }
  .net-weight {
    position: absolute; left: 675px; top: 26px;
    color: var(--white); font-size: 17px; font-weight: 400;
  }
  .title-band {
    position: absolute; left: 218px; top: 118px;
    width: 614px; height: 133px;
    background: var(--band-grey);
  }
  .product-name {
    position: absolute; left: 78px; top: 12px;
    font-size: 70px; font-weight: 900; line-height: 1;
    letter-spacing: -1px; color: var(--ink);
  }
  .product-type {
    position: absolute; left: 78px; top: 84px;
    font-size: 38px; font-weight: 300; line-height: 1;
    color: var(--ink); letter-spacing: -0.3px;
  }
  .flavour-band {
    position: absolute; left: 218px; top: 251px;
    width: 614px; height: 37px;
    background: var(--lemon);
  }
  .flavour-band span {
    position: absolute; left: 78px; top: 6px;
    font-size: 24px; font-weight: 500; color: var(--ink);
  }
  .stat {
    position: absolute; top: 316px;
    color: var(--white); text-align: center;
  }
  .stat .value { display: block; font-size: 18px; font-weight: 400; line-height: 1.05; }
  .stat .unit { display: block; font-size: 11px; font-weight: 400; }
  .claims {
    position: absolute; left: 218px; top: 364px; width: 614px;
    text-align: center; color: var(--soft-white);
    font-size: 16px; font-weight: 400;
  }
  .nutrition {
    position: absolute; left: 832px; top: 14px;
    width: 250px; height: 278px;
    border: 2px solid var(--white);
    color: var(--white);
    padding: 5px 7px;
  }
  .nutrition h2 { font-size: 17px; font-weight: 700; line-height: 1.1; }
  .nutrition .serving { font-size: 6.5px; padding-bottom: 4px; border-bottom: 2px solid var(--white); }
  .nutrition table { width: 100%; border-collapse: collapse; font-size: 7px; }
  .nutrition th { font-weight: 700; text-align: right; padding: 2px 0; }
  .nutrition thead tr.head-row th { text-align: right; border-bottom: 1px solid var(--white); }
  .nutrition td { padding: 3.3px 0; border-bottom: 0.5px solid #6a6a6a; text-align: right; }
  .nutrition td:first-child { text-align: left; }
  .nutrition td.sub { padding-left: 8px; }
  .ingredients {
    position: absolute; left: 832px; top: 298px; width: 252px;
    color: var(--white); font-size: 7px; line-height: 1.35;
  }
  .ingredients strong { font-weight: 700; }
  .ingredients .maker { margin-top: 4px; }
</style>
</head>
<body>
  <section class="label">
    <div class="carbon-fibre" role="img" aria-label="Carbon fibre weave background texture"></div>

    <aside class="info-panel">
      <p>Directions: Add 10g (approx. 2 scoops) into 500ml of chilly water depending on your liking, stir or shake to dissolve.</p>
      <p>Store below 30°C in a cool, dry place.</p>
      <p>Recommended Daily Intake: 1 serving.</p>
      <p class="tight">Formulated Supplementary Sports Food.</p>
      <p>This product is not a sole source of nutrition and should be consumed in conjunction with a nutritious diet and an appropriate physical training or exercise program.</p>
      <p>Not suitable for children under 15 years of age or pregnant women: Should only be used under medical or dietetic supervision.</p>
    </aside>

    <div class="brand-name">KORA<br>VITAL</div>
    <div class="net-weight">300G</div>

    <div class="title-band">
      <h1 class="product-name">HYDRATION</h1>
      <div class="product-type">ELECTROLYTE SUPPORT</div>
    </div>
    <div class="flavour-band"><span>LEMON FLAVOUR</span></div>

    <div class="stat" style="left:296px"><span class="value">1200mg</span><span class="unit">SODIUM</span></div>
    <div class="stat" style="left:427px"><span class="value">250mg</span><span class="unit">POTASSIUM</span></div>
    <div class="stat" style="left:551px"><span class="value">80mg</span><span class="unit">MAGNESIUM</span></div>
    <div class="stat" style="left:690px"><span class="value">30</span><span class="unit">SERVINGS</span></div>

    <div class="claims">GLUTEN FREE • NO ADDED SUGAR • NATURALLY FLAVOURED</div>

    <div class="nutrition">
      <h2>NUTRITION INFORMATION</h2>
      <div class="serving">SERVING SIZE: 10G · SERVINGS PER PACKAGE: 30</div>
      <table>
        <thead>
          <tr><th></th><th colspan="2" style="text-align:right">AVERAGE QUANTITY</th></tr>
          <tr class="head-row"><th></th><th>PER SERVING</th><th>PER 100G</th></tr>
        </thead>
        <tbody>
          <tr><td>Energy</td><td>34.6 kJ (8.3 Cal)</td><td>346 kJ (83 Cal)</td></tr>
          <tr><td>Protein</td><td>0.1 g</td><td>1.1 g</td></tr>
          <tr><td>Fat, Total</td><td>0.0 g</td><td>0.0 g</td></tr>
          <tr><td class="sub">-Saturated</td><td>0.0 g</td><td>0.0 g</td></tr>
          <tr><td>Carbohydrate</td><td>0.0 g</td><td>0.0 g</td></tr>
          <tr><td class="sub">-Sugars</td><td>0.0 g</td><td>0.0 g</td></tr>
          <tr><td>Dietary Fibre</td><td>3.9 g</td><td>39.0 g</td></tr>
          <tr><td>Sodium</td><td>1,200 mg</td><td>12,000 mg</td></tr>
          <tr><td>Potassium</td><td>250 mg</td><td>2,500 mg</td></tr>
          <tr><td>Calcium</td><td>80 mg</td><td>800 mg</td></tr>
          <tr><td>Magnesium</td><td>80 mg</td><td>800 mg</td></tr>
        </tbody>
      </table>
    </div>

    <div class="ingredients">
      <p><strong>INGREDIENTS:</strong> Electrolyte Minerals (Sodium Chloride, Magnesium Chloride, Potassium Chloride, Calcium Citrate), Acacia Gum, Natural Flavouring, Food Acid (Citric Acid), Sweetener (Thaumatin*), *Katemfe Fruit Extract.</p>
      <p class="maker"><strong>MANUFACTURED BY:</strong><br>LORE IPSUM<br>LORE IPSUM<br>LORE IPSUM</p>
    </div>
  </section>
</body>
</html>
```